Design a PowerPoint template for a consultancy organisation

I am after a Powerpoint template including three pages a title slide (that should have a title and subtitle), A title and content slide and a section header slide. I expect the company name and/or logo to be prominent and the colors to work well with the logo colors. I have included a copy of the logo

```html
<!DOCTYPE html>
<html lang="en">
<head>
<meta charset="utf-8">
<title>Parley Works – Presentation Template</title>
<link rel="stylesheet" href="https://fonts.googleapis.com/css2?family=Heebo:wght@700&family=Montserrat:wght@400;500;600&family=Arimo:wght@400&display=swap">
<style>
  :root {
    --stage: #bab8b9;
    --lavender: #efe7f5;
    --white: #ffffff;
    --green: #8dc63f;
    --purple: #6c12b0;
    --navy: #3d4e63;
    --powder: #a9c6d3;
    --frame: #5b4e8a;
    --body-text: #3d4e63;
    --muted-purple: #7a4f92;
  }
  * { box-sizing: border-box; margin: 0; padding: 0; }
  html, body { width: 710px; height: 1200px; overflow: hidden; }
  body { background: var(--stage); position: relative; font-family: "Montserrat", sans-serif; }

  .slide { position: absolute; width: 628px; height: 353px; background: var(--lavender); overflow: hidden; }
  .slide--title { left: 41px; top: 47px; }
  .slide--content { left: 45px; top: 438px; width: 620px; height: 349px; }
  .slide--section { left: 46px; top: 818px; width: 618px; height: 347px; }

  .slide__backdrop { position: absolute; inset: 0; width: 100%; height: 100%; }

  .brand-card {
    position: absolute; background: var(--white);
    display: flex; align-items: center; justify-content: center; gap: 4px;
  }
  .brand-mark { width: 8px; height: 8px; background: var(--green); }
  .brand-name { font-family: "Montserrat", sans-serif; font-weight: 600; font-size: 10.5px; color: var(--purple); white-space: nowrap; }

  .gradient-heading {
    position: absolute; font-family: "Heebo", sans-serif; font-weight: 700;
    letter-spacing: -1.2px; white-space: nowrap; line-height: 1;
    background: linear-gradient(90deg, var(--green) 0%, #8a8a72 40%, var(--muted-purple) 70%, var(--purple) 100%);
    -webkit-background-clip: text; background-clip: text; color: transparent;
  }

  .title-slide__heading { left: 0; width: 856px; text-align: center; top: 160px; font-size: 40px; transform: translateX(0); }
  .title-slide__text { position: absolute; left: 258px; width: 340px; text-align: center; }
  .title-slide__heading { left: 258px; width: 340px; }
  .title-slide__subtitle { top: 201px; font-size: 20px; font-weight: 600; color: var(--purple); }
  .title-slide__url { top: 285px; font-size: 10.5px; font-weight: 600; color: var(--purple); }

  .content-slide__brand { position: absolute; left: 520px; top: 26px; display: flex; align-items: center; gap: 4px; }
  .content-slide__brand .brand-name { font-size: 12px; }
  .content-slide__section-label {
    position: absolute; left: 40px; width: 130px; text-align: center; top: 170px; font-size: 20px;
    background: linear-gradient(90deg, var(--purple) 0%, var(--purple) 40%, #f2eef5 85%, var(--white) 100%);
    -webkit-background-clip: text; background-clip: text;
  }
  .content-slide__heading { position: absolute; left: 266px; top: 80px; font-size: 23px; font-weight: 400; color: var(--purple); white-space: nowrap; }
  .content-slide__rule { position: absolute; left: 266px; top: 141px; width: 16px; height: 3px; background: var(--green); }

  .feature-list { position: absolute; top: 169px; list-style: none; }
  .feature-list--first { left: 266px; }
  .feature-list--second { left: 376px; }
  .feature-list__item { display: flex; align-items: center; height: 24.5px; font-size: 10px; font-weight: 500; color: var(--navy); letter-spacing: 0.2px; }
  .feature-list__box { width: 12px; height: 12px; border: 3.5px solid currentColor; background: var(--white); margin-right: 10px; flex: none; }
  .feature-list__box--purple { color: var(--purple); }
  .feature-list__box--navy { color: var(--navy); }
  .feature-list__box--powder { color: var(--powder); }

  .product-visual { position: absolute; left: 477px; top: 152px; width: 101px; height: 93px; }
  .product-visual__fill { position: absolute; left: 12px; top: 13px; width: 78px; height: 67px; background: linear-gradient(135deg, #bfe08f, var(--green)); opacity: 0.55; }

  .content-slide__body { position: absolute; left: 265px; top: 258px; width: 310px; font-family: "Arimo", sans-serif; font-size: 9.6px; line-height: 15.1px; color: var(--body-text); }

  .section-slide__heading { left: 282px; top: 160px; font-size: 39px; }
</style>
</head>
<body>

  <!-- Title slide -->
  <section class="slide slide--title">
    <svg class="slide__backdrop" viewBox="0 0 1312 738" preserveAspectRatio="none" aria-hidden="true">
      <rect width="1312" height="738" fill="var(--lavender)"/>
      <rect width="77" height="738" fill="var(--white)"/>
      <circle cx="244" cy="382" r="260" fill="var(--white)"/>
      <path d="M0 283 C60 283 98 272 110 252 L110 512 C98 492 60 481 0 481 Z" fill="var(--green)"/>
      <circle cx="244" cy="383" r="184" fill="var(--green)"/>
    </svg>
    <div class="brand-card" style="left:68px; top:159px; width:88px; height:49px;">
      <span class="brand-mark"></span><span class="brand-name">Parley Works</span>
    </div>
    <h1 class="gradient-heading title-slide__heading">Marketing Strategy</h1>
    <p class="title-slide__text title-slide__subtitle">Presentation Subtitle</p>
    <p class="title-slide__text title-slide__url">www.parleyworks.com</p>
  </section>

  <!-- Title and content slide -->
  <section class="slide slide--content">
    <svg class="slide__backdrop" viewBox="0 0 1312 738" preserveAspectRatio="none" aria-hidden="true">
      <rect width="1312" height="738" fill="var(--lavender)"/>
      <rect width="77" height="738" fill="var(--white)"/>
      <circle cx="244" cy="382" r="260" fill="var(--white)"/>
      <path d="M0 283 C60 283 98 272 110 252 L110 512 C98 492 60 481 0 481 Z" fill="var(--green)"/>
      <circle cx="244" cy="383" r="184" fill="var(--green)"/>
    </svg>
    <div class="content-slide__brand">
      <span class="brand-mark"></span><span class="brand-name">Parley Works</span>
    </div>
    <p class="gradient-heading content-slide__section-label">Dunctionality</p>
    <h2 class="content-slide__heading">Product features list</h2>
    <div class="content-slide__rule"></div>

    <ul class="feature-list feature-list--first">
      <li class="feature-list__item"><span class="feature-list__box feature-list__box--purple"></span>Feature One</li>
      <li class="feature-list__item"><span class="feature-list__box feature-list__box--navy"></span>Feature Two</li>
      <li class="feature-list__item"><span class="feature-list__box feature-list__box--powder"></span>Feature Three</li>
    </ul>
    <ul class="feature-list feature-list--second">
      <li class="feature-list__item"><span class="feature-list__box feature-list__box--purple"></span>Feature Four</li>
      <li class="feature-list__item"><span class="feature-list__box feature-list__box--navy"></span>Feature Five</li>
      <li class="feature-list__item"><span class="feature-list__box feature-list__box--powder"></span>Feature Six</li>
    </ul>

    <div class="product-visual">
      <svg width="101" height="93" viewBox="0 0 101 93" aria-hidden="true">
        <polyline points="2,47 2,1 55,1" fill="none" stroke="var(--frame)" stroke-width="3"/>
        <polyline points="40,92 99,92 99,54" fill="none" stroke="var(--frame)" stroke-width="3"/>
      </svg>
      <div class="product-visual__fill" role="img" aria-label="Illustration of an open product box"></div>
    </div>

    <p class="content-slide__body">Lorem ipsum dolor sit amet, consectetuer adipiscing elit. Aenean commodo ligula eget dolor. Aenean massa. Cum sociis natoque penatibus et magnis dis parturient montes, nascetur ridiculus mus. Donec quam felis, ultricies nec, pellentesque eu, pretium quis, sem.</p>
  </section>

  <!-- Section header slide -->
  <section class="slide slide--section">
    <svg class="slide__backdrop" viewBox="0 0 1312 738" preserveAspectRatio="none" aria-hidden="true">
      <rect width="1312" height="738" fill="var(--lavender)"/>
      <rect width="77" height="738" fill="var(--white)"/>
      <circle cx="244" cy="382" r="260" fill="var(--white)"/>
      <path d="M0 283 C60 283 98 272 110 252 L110 512 C98 492 60 481 0 481 Z" fill="var(--green)"/>
      <circle cx="244" cy="383" r="184" fill="var(--green)"/>
    </svg>
    <div class="brand-card" style="left:67px; top:156px; width:87px; height:48px;">
      <span class="brand-mark"></span><span class="brand-name">Parley Works</span>
    </div>
    <h2 class="gradient-heading section-slide__heading">Section Title</h2>
  </section>

</body>
</html>
```